The Heron Wand for the Company The Velvet Bayou

This vibrator is a sex toy. It will represent the brand from the Velvet Bayou which is an upcoming adult novelty wholesale company. This will be our first vibrator on the market. Looking for a cajun-southern-louisiana touch. Fun, classy, feminine, and eye catching. I am looking for packaging that will be appealing to boutique style adult novelty stores. I will attach the Velvet Bayou logo. The vibrator will have dual power options and made of high quality grade materials....which means it will be a higher end toy like the MIRVA. I have attached the logo for The Velvet Bayou which is the business name in addition to a vibrator which will be close in the style choice of our design. The Velvet Bayou is a sister company of Hold Me Silks.

Target Market(s)

Females ages 18-60. Middle class with an eye for class and style.

Industry/Entity Type

Retail

Colors
eda3c7
e667a6
e34297
b7a5cd
876aae
6b449b
ffffff
9d9d9d
1b1b1b

Requirements
Must have
• The name of the Product is "the Heron Wand" (without parenthesis)
• The name of the company is the Velvet Bayou.
• The packaging will be a see-through on the front and not see through on the back. (not sure if that is significant) but I want a catchy logo for the name in addition to a picture which corresponds to the Velvet Bayou. Colors I am not too sure about. Packaging is key and the target would include women; so extremely feminine and eye catching. CLASS, FEMININE.....
• I want all retailers to want to put this item in their store.
Nice to have
• a Gator picture incorporated with the logo. Creative flare and female driven design. Soft and elegant - fun, sexy, trendy.

```html
<!DOCTYPE html>
<html lang="en">
<head>
<meta charset="utf-8">
<title>The Heron Wand – Hang Tag Packaging</title>
<link rel="stylesheet" href="https://fonts.googleapis.com/css2?family=Open+Sans:wght@400;600&display=swap">
<style>
  :root {
    --stage: #1b1b1b;
    --rule: #ffffff;
    --card-grey: #e0e0e0;
    --card-edge: #9d9d9d;
    --magenta: #d4418c;
    --blush: #e8a0c5;
    --white: #ffffff;
    --ink: #1b1b1b;
    --tab-deep: #6b449b;
    --tab-soft: #b7a5cd;
    --brand: #e34297;
  }
  * { margin: 0; padding: 0; box-sizing: border-box; }
  html, body {
    width: 849px; height: 1200px; overflow: hidden;
    background: var(--stage);
    font-family: "Open Sans", Arial, sans-serif;
  }
  .artboard { position: relative; width: 849px; height: 1200px; }
  .artboard-shapes { position: absolute; inset: 0; }
  .card-artwork {
    position: absolute; left: 431px; top: 321px; width: 254px; height: 580px;
    border-radius: 2px;
    background: linear-gradient(110deg, var(--card-grey) 0%, var(--card-grey) 35%, var(--blush) 58%, var(--magenta) 85%);
  }
  .dimension-label {
    position: absolute; color: var(--rule);
    font-size: 26px; line-height: 1; white-space: nowrap;
  }
  .dimension-label--height { left: 80px; top: 529px; }
  .dimension-label--width { left: 558px; top: 1030px; transform: translateX(-50%); }
  .brand-name {
    position: absolute; left: 557px; top: 283px; transform: translateX(-50%);
    color: var(--brand); font-size: 21px; font-weight: 400; white-space: nowrap;
  }
  .product-title {
    position: absolute; left: 455px; top: 339px; width: 214px; height: 28px;
    border-top: 1.5px solid var(--ink); border-bottom: 1.5px solid var(--ink);
    text-align: center; color: var(--ink);
    font-size: 21px; line-height: 25px; white-space: nowrap;
  }
  .tagline {
    position: absolute; color: var(--ink); font-size: 16px; line-height: 20px; white-space: nowrap;
  }
  .tagline--first { left: 443px; top: 837px; }
  .tagline--second { left: 467px; top: 864px; }
</style>
</head>
<body>
<div class="artboard">
  <svg class="artboard-shapes" width="849" height="1200" viewBox="0 0 849 1200">
    <g class="dimension-height" stroke="var(--rule)" stroke-width="2" fill="none">
      <line x1="152" y1="162" x2="398" y2="162"/>
      <line x1="152" y1="902" x2="398" y2="902"/>
      <line x1="170" y1="162" x2="170" y2="902"/>
    </g>
    <g class="dimension-width" stroke="var(--rule)" stroke-width="2" fill="none">
      <line x1="430" y1="928" x2="430" y2="1026"/>
      <line x1="686" y1="928" x2="686" y2="1026"/>
      <line x1="430" y1="1022" x2="686" y2="1022"/>
    </g>

    <g class="hang-tab">
      <path d="M518 218 V190 Q518 162 546 162 H566 Q594 162 594 190 V218 Z" fill="var(--tab-soft)"/>
      <path d="M518 218 V190 Q518 162 546 162 H566 Q540 175 530 218 Z" fill="var(--tab-deep)"/>
      <circle cx="555" cy="173" r="4.5" fill="var(--stage)"/>
    </g>

    <path class="header-dome" d="M442 320 C442 255 495 213 557 213 C619 213 672 255 672 320 Z"
          fill="var(--white)" stroke="var(--card-edge)" stroke-width="2"/>

    <rect class="card-edge" x="430" y="320" width="256" height="582" rx="3"
          fill="var(--card-grey)" stroke="var(--card-edge)" stroke-width="2"/>
  </svg>

  <div class="card-artwork" role="img" aria-label="Flowing pink and white wave artwork across the card front"></div>

  <div class="dimension-label dimension-label--height">20cm</div>
  <div class="dimension-label dimension-label--width">8 cm</div>

  <div class="brand-name">Velvet Bayou</div>
  <div class="product-title">the Heron Wand</div>
  <p class="tagline tagline--first">Extra enjoy .....</p>
  <p class="tagline tagline--second">Extra excite .....</p>
</div>
</body>
</html>
```